Digital Album Cover - Where The Quiet River Bends (Piano & Cello)

HiI would like a digital album coverTitle: "Where The Quiet River Bends (Piano & Cello)"Artist: "Lorcan Pettigrew & The Oduya Priscilla"

• Original creativity
• Copyrighted images

```html
<!DOCTYPE html>
<html lang="en">
<head>
<meta charset="utf-8">
<title>Where The Quiet River Bends (Piano &amp; Cello) – Album Cover</title>
<link rel="stylesheet" href="https://fonts.googleapis.com/css2?family=Josefin+Sans:wght@100;300;400&display=swap">
<style>
  :root {
    --bg-night: #1f1b1d;
    --tone-warm: #6b4a2c;
    --tone-ochre: #a77a3c;
    --tone-red: #8c2f2a;
    --tone-blue: #5d6f8c;
    --band-veil: rgba(255, 255, 255, 0.34);
    --type-light: #f6f3ef;
  }
  * { margin: 0; padding: 0; box-sizing: border-box; }
  html, body {
    width: 1200px;
    height: 1200px;
    overflow: hidden;
    background: var(--bg-night);
  }
  .album-cover {
    position: relative;
    width: 1200px;
    height: 1200px;
    overflow: hidden;
    background: var(--bg-night);
  }
  .cover-artwork {
    position: absolute;
    inset: 0;
    background:
      radial-gradient(ellipse 38% 45% at 48% 52%, var(--tone-ochre) 0%, var(--tone-warm) 45%, transparent 75%),
      radial-gradient(ellipse 30% 40% at 80% 40%, var(--tone-red) 0%, transparent 70%),
      radial-gradient(ellipse 25% 30% at 30% 15%, var(--tone-red) 0%, transparent 70%),
      radial-gradient(ellipse 25% 30% at 70% 12%, var(--tone-blue) 0%, transparent 70%),
      radial-gradient(ellipse 30% 30% at 10% 80%, var(--tone-red) 0%, transparent 70%),
      var(--bg-night);
  }
  .diagonal-band {
    position: absolute;
    inset: 0;
    width: 1200px;
    height: 1200px;
  }
  .diagonal-band polygon { fill: var(--band-veil); }
  .cover-title {
    position: absolute;
    left: 78px;
    right: 56px;
    top: 1052px;
    font-family: "Josefin Sans", sans-serif;
    font-weight: 100;
    font-size: 66px;
    line-height: 1;
    letter-spacing: 1px;
    text-transform: uppercase;
    color: var(--type-light);
    white-space: nowrap;
    text-align: right;
  }
  .cover-artist {
    position: absolute;
    right: 58px;
    top: 1130px;
    font-family: "Josefin Sans", sans-serif;
    font-weight: 400;
    font-size: 14px;
    letter-spacing: 4px;
    text-transform: uppercase;
    color: var(--type-light);
    white-space: nowrap;
  }
</style>
</head>
<body>
  <main class="album-cover">
    <div class="cover-artwork" role="img" aria-label="Painted illustration of an embracing couple in knit sweaters against a backdrop of red, white and blue bokeh lights"></div>

    <svg class="diagonal-band" viewBox="0 0 1200 1200" aria-hidden="true">
      <polygon points="0,467 0,1200 735,1200"/>
    </svg>

    <h1 class="cover-title">Where The Quiet River Bends</h1>
    <p class="cover-artist">Lorcan Pettigrew &amp; The Oduya Priscilla</p>
  </main>
</body>
</html>
```